indépendant en tant que Massothérapeute et Préparateur Mental, j'ai besoin de ...

Massothérapeute et préparateur mental indépendant, je recherche une carte de visite sobre et dynamique, sans images liées au massage ou à la préparation mentale mais intégrant mon logo. Les couleurs que j'aime bien sont : Blanc, gris, anthracite, noir et jaune

Contact Information for Business Card

carte de préférence Horizontale
neutre qui puisse toucher le deux domaines Massothérapie et préparation mentale

Requirements
Must have
• mon projet doit intégrer au recto:
LOGO
Loïc Vermande
078 315 26 49
info@loicvermande-exemple.ch
et éventuellement www.loicvermande-exemple.ch

et au verso les deux adresses:

Chemin des Ormelets 27B
1400 Yverdon-les-Bains

Rue des Tanneries 9
1700 Fribourg

Should not have
• mon projet ne doit pas contenir d'image en liens avec le massage ni la préparation mentale.

```html
<!DOCTYPE html>
<html lang="fr">
<head>
<meta charset="utf-8">
<title>Loïc Vermande – cartes de visite</title>
<link rel="stylesheet" href="https://fonts.googleapis.com/css2?family=Ubuntu:wght@400;500;700&display=swap">
<style>
  :root {
    --backdrop: #2a2a2a;
    --black: #1d1c1d;
    --anthracite: #2c2b2d;
    --grey: #5c5c5e;
    --grey-dark: #454547;
    --white: #f7f7f7;
    --yellow: #c6dd14;
    --ink-on-grey: #232323;
  }
  * { box-sizing: border-box; margin: 0; padding: 0; }
  html, body { width: 1200px; height: 900px; overflow: hidden; }
  body {
    background: var(--backdrop);
    font-family: "Ubuntu", sans-serif;
    position: relative;
  }
  .card {
    position: absolute;
    width: 560px;
    height: 350px;
    overflow: hidden;
    box-shadow: 0 14px 30px rgba(0,0,0,.55);
  }
  .card-back { left: 70px; top: 60px; background: var(--white); }
  .card-front { left: 570px; top: 490px; background: var(--black); }
  .card-shapes { position: absolute; inset: 0; width: 100%; height: 100%; }

  .brand {
    position: absolute;
    display: flex;
    flex-direction: column;
    white-space: nowrap;
  }
  .brand-name {
    display: flex;
    align-items: center;
    gap: 10px;
    font-weight: 700;
    font-size: 28px;
    letter-spacing: .3px;
    line-height: 1.1;
  }
  .brand-dot {
    width: 20px; height: 20px; border-radius: 50%;
    background: currentColor;
    flex: none;
  }
  .brand-tagline {
    font-size: 10px;
    font-weight: 500;
    letter-spacing: .4px;
    font-variant: small-caps;
    margin-top: 6px;
    padding-left: 30px;
  }
  .card-back .brand { left: 318px; top: 42px; color: var(--black); }
  .card-back .brand-name { font-size: 26px; }
  .card-front .brand { left: 30px; top: 205px; color: var(--white); }

  .addresses {
    position: absolute;
    left: 34px; top: 118px;
    list-style: none;
    color: var(--white);
    font-size: 16px;
    line-height: 1.3;
  }
  .addresses li { display: flex; gap: 10px; margin-bottom: 22px; }
  .addresses svg { flex: none; margin-top: 16px; }

  .contact {
    position: absolute;
    left: 330px; top: 70px;
    color: var(--ink-on-grey);
  }
  .contact-name { font-size: 28px; font-weight: 700; margin-bottom: 22px; white-space: nowrap; }
  .contact-list { list-style: none; font-size: 13.5px; line-height: 1.75; }
  .contact-list li { display: flex; align-items: center; gap: 8px; white-space: nowrap; }
</style>
</head>
<body>

<section class="card card-back" aria-label="Verso de la carte">
  <svg class="card-shapes" viewBox="0 0 560 350" preserveAspectRatio="none" aria-hidden="true">
    <polygon points="0,0 210,0 316,108 230,350 0,350" fill="var(--grey-dark)"/>
    <polygon points="190,0 206,0 312,108 226,350 212,350 298,108" fill="var(--yellow)"/>
    <polygon points="0,0 192,0 296,108 212,350 0,350" fill="var(--black)"/>
  </svg>

  <div class="brand">
    <div class="brand-name"><span class="brand-dot"></span>Loïc Vermande</div>
    <div class="brand-tagline">Massothérapeute / Préparateur Mental</div>
  </div>

  <ul class="addresses">
    <li>
      <svg width="11" height="14" viewBox="0 0 11 14"><path d="M5.5 0A5.5 5.5 0 0 0 0 5.5C0 9.5 5.5 14 5.5 14S11 9.5 11 5.5A5.5 5.5 0 0 0 5.5 0Zm0 7.6a2 2 0 1 1 0-4 2 2 0 0 1 0 4Z" fill="var(--white)"/></svg>
      <span>Chemin des Ormelets 27B<br>1400 Yverdon-les-Bains</span>
    </li>
    <li>
      <svg width="11" height="14" viewBox="0 0 11 14"><path d="M5.5 0A5.5 5.5 0 0 0 0 5.5C0 9.5 5.5 14 5.5 14S11 9.5 11 5.5A5.5 5.5 0 0 0 5.5 0Zm0 7.6a2 2 0 1 1 0-4 2 2 0 0 1 0 4Z" fill="var(--white)"/></svg>
      <span>Rue des Tanneries 9<br>1700 Freiburg</span>
    </li>
  </ul>
</section>

<section class="card card-front" aria-label="Recto de la carte">
  <svg class="card-shapes" viewBox="0 0 560 350" preserveAspectRatio="none" aria-hidden="true">
    <polygon points="262,0 560,0 560,350 420,350 236,170" fill="var(--grey-dark)"/>
    <polygon points="250,0 264,0 240,170 424,350 406,350 226,170" fill="var(--yellow)"/>
    <polygon points="278,0 560,0 560,350 438,350 254,170" fill="var(--grey)"/>
  </svg>

  <div class="brand">
    <div class="brand-name"><span class="brand-dot"></span>Loïc Vermande</div>
    <div class="brand-tagline">Massothérapeute / Préparateur Mental</div>
  </div>

  <div class="contact">
    <p class="contact-name">Loïc Vermande</p>
    <ul class="contact-list">
      <li>
        <svg width="12" height="12" viewBox="0 0 12 12"><path d="M2.4 0.6 4.2 2.6 3.3 4.1C4 5.7 6.3 8 7.9 8.7L9.4 7.8 11.4 9.6 10.2 11.4C6 11.4 0.6 6 0.6 1.8Z" fill="var(--ink-on-grey)"/></svg>
        078 315 26 49
      </li>
      <li>
        <svg width="13" height="11" viewBox="0 0 13 11"><rect x="0.5" y="1" width="12" height="9" rx="1" fill="var(--ink-on-grey)"/><path d="M1 1.8 6.5 6 12 1.8" stroke="var(--grey)" stroke-width="1.2" fill="none"/></svg>
        info@loicvermande-exemple.ch
      </li>
      <li>
        <svg width="12" height="12" viewBox="0 0 12 12"><circle cx="6" cy="6" r="5.5" fill="var(--ink-on-grey)"/><path d="M0.8 6H11.2M6 0.5C3.5 3.5 3.5 8.5 6 11.5M6 0.5C8.5 3.5 8.5 8.5 6 11.5" stroke="var(--grey)" stroke-width=".8" fill="none"/></svg>
        www.loicvermande-exemple.ch
      </li>
    </ul>
  </div>
</section>

</body>
</html>
```